Luxurious Product label and box for all natural skincare product. + 30AUD tip to winner.

What I require.
1.     One product label and one-box design.
2.     I must have a mock-up of the bottle with the attached label and the box.
 
I have supplied the following files for the designers to use.
1.     Brand logo file. (logo.zip)
2.     Slogan file. (slogan.psd)
3.     Slogan script file. (italianno.regular.ttf)
4.     Bottle image file. (60ml_moisturiser_bottle.png)
5.     Icon bar file. (Icon_bar_en.zip)
 
Label and box Design
I am interested in your unique design concepts and colors, so please feel free to be creative.
1.     Brand name: Velmora
2.     You can use your own choice of colors in your design. I would prefer two colors (excluding logo and slogan colors), although more colors are acceptable for the right design.
3.     Label and box to have a background color or pattern.
4.     I would like the icon bar to wrap around the bottom of the label and box, covering the full width of all sides of the box.
5.     The height of the icon bar should be about 7mm to 10mm high.   
6.     The hex code for the icon bar color is #EDD6D4. The color of the icons can be any color the designer chooses.
7.     The positioning of the icons are as follows.
a)     The front panel has three icons. From left to right, they are; 100% Vegan, Product of Australia, and 100% Natural.
b)     The left side panel has three icons. From the front of the label/box to the back of the label/box, they are; Cruelty-Free, Ethical & Sustainable, and Please Recycle.
c)     The right side panel has only one icon situated at the front of the right side of the label/box. The icon is 6 Months Once Open.
 
Label.
1.     The label will be a three-panel label.
2.     The label will contain text in all three panels; however, only the text for the front panel of the label is supplied in this brief. For now, use Lorem Ipsum placeholder text to fill spaces.
3.     The final text will be provided to the winning designer so they can apply the text to the left and right panels of the label.
4.     Label size. Width 104mm x Height 83mm.
5.     The final design file must include bleed and cut lines.
 
Box.
1.     The box will contain text on all four sides; however, only the text for the front of the box is supplied in this brief. For now, use Lorem Ipsum placeholder text to fill spaces.
2.     The final text will be provided to the winning designer so they can apply the text to the left and right sides and the back of the box.
3.     The box size is 40mm wide x 40mm deep x 140mm high.
4.     The final design file must include bleed and cut lines.
 
Front Panel wording.
1.     Logo.
2.     Slogan.
3.     Moisturiser.
4.     Hydrate & Nourish.
5.     Hyaluronic Acid, Desert Lime & Green Tea.
6.     All Skin Types - Dry – Dehydrated.
7.     Icon bar.
8.     60mL
 
Bottle size
60ml White Bottle – 13.5cm High x 3.5cm Wide.

Target Market(s)

Beauty-minded Asian consumers between the age of 32 and 75 who take a proactive approach in maintaining younger-looking skin. Those who already know the danger of damaged skin caused by skincare containing harsh chemicals, and therefore choose effective natural/organic solutions to meet their skincare needs. Those who wish a more radiant glow and youthful appearance to their skin. Usually, a two-income middle to high-income bracket couple with a mindset for health and beauty.

Industry/Entity Type

Beauty and skincare.

Font styles to use
Other font styles liked:
• Logo and slogan script supplied. Designer to choose all other font or script.

Colors

Designer to choose colors to be used in the design.

Requirements
Must have
• A mock-up label on the bottle and a mock-up box. My logo and slogan are already designed with my chosen font and color.
Nice to have
• I like soft pastel colors with perhaps a small amount of stronger color.

```html
<!DOCTYPE html>
<html lang="en">
<head>
<meta charset="utf-8">
<title>Velmora Moisturiser – Label and Box</title>
<link href="https://fonts.googleapis.com/css2?family=Exo+2:wght@400;500&display=swap" rel="stylesheet">
<style>
  :root{
    --sky:#00a2ff;
    --gold-light:#f3dc8a;
    --gold:#d9ae4e;
    --wine:#7f1520;
    --crimson:#d0185a;
    --rose:#ee1f6b;
    --blush:#f2708f;
    --ink:#231f20;
    --cream:#f6e4e4;
    --iconbar:#EDD6D4;
  }
  *{margin:0;padding:0;box-sizing:border-box}
  html,body{width:1200px;height:910px;overflow:hidden;background:var(--sky)}
  body{position:relative;font-family:"Exo 2",sans-serif}

  .piece{position:absolute;overflow:hidden}
  .label{left:341px;top:406px;width:164px;height:388px;border-radius:0 0 8px 8px}
  .box{left:542px;top:105px;width:297px;height:686px}

  .gold-band{position:absolute;left:0;right:0;background:linear-gradient(90deg,var(--gold),var(--gold-light) 30%,var(--gold-light) 70%,var(--gold))}
  .field{position:absolute;left:0;right:0;background:linear-gradient(180deg,var(--wine) 0%,var(--crimson) 38%,var(--rose) 60%,var(--blush) 100%)}
  .icon-bar{position:absolute;left:0;right:0;bottom:0;background:var(--iconbar)}

  .brand-band{position:absolute;left:0;right:0;background:var(--ink);border-top:solid var(--gold);border-bottom:solid var(--gold);display:flex;align-items:center;justify-content:center}
  .brand{color:var(--gold);font-weight:500;letter-spacing:.02em;line-height:1}

  .title-band{position:absolute;left:0;right:0;background:var(--ink);border-top:solid var(--gold);border-bottom:solid var(--gold);color:var(--cream);text-align:center}
  .line{position:absolute;left:0;right:0;text-align:center;white-space:nowrap}
  .tagline{color:var(--cream)}
  .ingredients{color:var(--cream)}
  .skin{color:var(--ink)}
  .volume{position:absolute;left:0;right:0;text-align:center;color:var(--ink)}

  /* box sizes */
  .box .top-band{top:0;height:21px}
  .box .field{top:21px;height:545px}
  .box .brand-band{top:72px;height:190px;border-width:7px}
  .box .brand{font-size:72px}
  .box .title-band{top:347px;height:57px;border-width:5px;font-size:44px;line-height:46px}
  .box .tagline{top:406px;font-size:24px}
  .box .ingredients{top:447px;font-size:15px}
  .box .skin{top:500px;font-size:15px}
  .box .volume-band{top:566px;height:45px}
  .box .volume{top:570px;font-size:27px;line-height:36px}
  .box .icon-bar{height:75px}

  /* label sizes */
  .label .top-band{top:0;height:12px}
  .label .field{top:12px;height:300px}
  .label .brand-band{top:40px;height:110px;border-width:4px}
  .label .brand{font-size:38px}
  .label .title-band{top:187px;height:31px;border-width:3px;font-size:24px;line-height:24px}
  .label .tagline{top:220px;font-size:12.5px}
  .label .ingredients{top:243px;font-size:7.5px}
  .label .skin{top:271px;font-size:7px}
  .label .volume-band{top:304px;height:25px}
  .label .volume{top:307px;font-size:14px;line-height:18px}
  .label .icon-bar{height:59px}

  .icons{position:absolute;left:0;right:0;bottom:8px;display:flex;justify-content:space-around;padding:0 6px}
  .icon{display:flex;flex-direction:column;align-items:center;font-size:3.6px;font-weight:500;color:var(--ink);line-height:1.2;text-align:center}
  .icon svg{width:16px;height:16px;margin-bottom:2px}
</style>
</head>
<body>

<section class="piece label" aria-label="Bottle label front panel">
  <div class="gold-band top-band"></div>
  <div class="field"></div>
  <div class="brand-band"><span class="brand">Velmora</span></div>
  <div class="title-band">Moisturiser</div>
  <div class="line tagline">Hydrate &amp; Nourish</div>
  <div class="line ingredients">Hyaluronic Acid • Desert Lime • Green Tea.</div>
  <div class="line skin">All Skin Types – Dry – Dehydrated.</div>
  <div class="gold-band volume-band"></div>
  <div class="volume">60mL</div>
  <div class="icon-bar">
    <div class="icons">
      <div class="icon">
        <svg viewBox="0 0 16 16" aria-hidden="true"><path d="M8 14 C2 9 1 6 3 4 C5 2 7 3 8 5 C9 3 11 2 13 4 C15 6 14 9 8 14Z" fill="none" stroke="#231f20" stroke-width="1"/></svg>
        100%<br>Vegan
      </div>
      <div class="icon">
        <svg viewBox="0 0 16 16" aria-hidden="true"><circle cx="8" cy="8" r="6" fill="none" stroke="#231f20" stroke-width="1"/></svg>
        Product of<br>Australia
      </div>
      <div class="icon">
        <svg viewBox="0 0 16 16" aria-hidden="true"><path d="M8 14 C4 11 4 6 8 2 C12 6 12 11 8 14Z M8 14 L8 6" fill="none" stroke="#231f20" stroke-width="1"/></svg>
        100%<br>Natural
      </div>
    </div>
  </div>
</section>

<section class="piece box" aria-label="Box front panel">
  <div class="gold-band top-band"></div>
  <div class="field"></div>
  <div class="brand-band"><span class="brand">Velmora</span></div>
  <div class="title-band">Moisturiser</div>
  <div class="line tagline">Hydrate &amp; Nourish</div>
  <div class="line ingredients">Hyaluronic Acid • Desert Lime • Green Tea.</div>
  <div class="line skin">All Skin Types – Dry – Dehydrated.</div>
  <div class="gold-band volume-band"></div>
  <div class="volume">60mL</div>
  <div class="icon-bar"></div>
</section>

</body>
</html>
```